Coastal Heritage Dairywrights' Guild needs new business cards

We need new business cards designed and produced. We are likely to need other design work done for ads, flyers etc in future.

We would like to start with an initial business card.

The Coastal Heritage Dairywrights' Guild (CHDG) is a membership-based not-for-profit organisation that looks after the interests of Australia's small to medium artisan cheesemakers, many of whom are also small-scale farmers. The design should be simple, using our logo, but also communicate our artisan cheese and small dairy farm focus.

The first card to be designed and produced is for me, Megan Thorburn. My details are:

Megan Thorburn
Secretary
Coastal Heritage Dairywrights' Guild (CHDG)
http://www.curdandcrockery.org
T +61427583914
E megan.meganthorburn@mailfern.net

I have attached the CHDG logo in jpg form. I have a higher resolution version available if needed.

Thank you!

Megan

Business

Megan Thorburn
Coastal Heritage Dairywrights' Guild
megan.meganthorburn@mailfern.net
+61427583914

Sans Serif

• Logo (see attached file)

```html
<!DOCTYPE html>
<html lang="en">
<head>
<meta charset="utf-8">
<title>CHDG Business Card – Megan Thorburn</title>
<link rel="stylesheet" href="https://fonts.googleapis.com/css2?family=Source+Sans+3:wght@400;600&display=swap">
<style>
  :root {
    --stage: #000000;
    --brown: #5e3819;
    --butter: #fdce6b;
    --cream: #ffffff;
    --ink-brown: #5a3719;
  }
  * { margin: 0; padding: 0; box-sizing: border-box; }
  html, body { width: 1200px; height: 900px; overflow: hidden; background: var(--stage); }
  body { position: relative; font-family: "Source Sans 3", "Myriad Pro", Arial, sans-serif; }

  .card { position: absolute; top: 275px; width: 477px; height: 294px; }
  .card--front { left: 116px; background: var(--brown); border-radius: 0 46px 0 46px; }
  .card--back { left: 622px; top: 276px; height: 293px; background: var(--butter); border-radius: 46px 0 46px 0; }

  .brand { position: absolute; display: flex; align-items: center; }
  .brand__dot { border-radius: 50%; flex: none; }
  .brand__name { line-height: 1.16; font-weight: 400; }

  .card--front .brand { left: 231px; top: 44px; }
  .card--front .brand__dot { width: 84px; height: 84px; border: 2px solid var(--cream); margin-right: 13px; }
  .card--front .brand__name { color: var(--cream); font-size: 19px; }

  .card--back .brand { left: 91px; top: 90px; }
  .card--back .brand__dot { width: 112px; height: 112px; border: 2px solid var(--ink-brown); margin-right: 14px; }
  .card--back .brand__name { color: var(--ink-brown); font-size: 24px; }

  .holder { position: absolute; left: 29px; top: 170px; color: var(--butter); }
  .holder__name { font-size: 18px; font-weight: 600; line-height: 1.2; }
  .holder__role { font-size: 13px; margin-top: 4px; }

  .contacts { position: absolute; right: 20px; top: 206px; list-style: none; color: var(--butter); font-size: 13px; text-align: right; }
  .contacts li { display: flex; justify-content: flex-end; align-items: center; height: 20px; }
  .contacts svg { width: 10px; height: 10px; margin-left: 8px; fill: var(--butter); }
</style>
</head>
<body>
  <section class="card card--front">
    <div class="brand">
      <span class="brand__dot"></span>
      <p class="brand__name">Coastal<br>Heritage<br>Dairywrights'<br>Guild</p>
    </div>
    <div class="holder">
      <p class="holder__name">Megan Thorburn</p>
      <p class="holder__role">Secretary</p>
    </div>
    <ul class="contacts">
      <li>+61427583914
        <svg viewBox="0 0 10 10"><path d="M2 0.5 L3.8 2.6 L2.9 3.6 Q4 5.9 6.4 7.1 L7.4 6.2 L9.5 8 L8.4 9.5 Q3.8 9 0.5 1.6 Z"/></svg></li>
      <li>megan.meganthorburn@mailfern.net
        <svg viewBox="0 0 10 10"><path d="M0.5 2 H9.5 V8 H0.5 Z M1 2.5 L5 5.5 L9 2.5" fill="var(--butter)" stroke="var(--brown)" stroke-width="0.8"/></svg></li>
      <li>www.curdandcrockery.org
        <svg viewBox="0 0 10 10"><circle cx="5" cy="5" r="4.5"/><path d="M5 0.5 V9.5 M0.5 5 H9.5 M5 0.5 Q2 5 5 9.5 M5 0.5 Q8 5 5 9.5" fill="none" stroke="var(--brown)" stroke-width="0.7"/></svg></li>
    </ul>
  </section>

  <section class="card card--back">
    <div class="brand">
      <span class="brand__dot"></span>
      <p class="brand__name">Coastal<br>Heritage<br>Dairywrights'<br>Guild</p>
    </div>
  </section>
</body>
</html>
```